Clean A3 Menu Brochure for a Pizza Shop

We are looking for a cleaner design to replace our old menu (please find attached) and we already have a draft (please find attached). The menu should be A3 and easy to read with a very subtle marble background and clean font for the menu items. It can be folded for leafleting or be used flat on the store counter. It should not be overcrowded, and the prices for each item should be easy to understand. Ideally we would like images for each section in the menu body, for example chicken for the Chicken Sides (feel free to leave space or add any photos - these will be replaced with our own photos in a later revision) and these should feel natural to the menu (please see Inspo pictures). The deals will be split into 2 sections: The main 3 deals which will come with photos once we do a photoshoot and a more compact list of all the other deals. We have left the front page quite empty as we’re not sure what will go on it, except for 1 large image like in the old menu, our store details and that we can be found on FeastDrop, RapidBite and Platecarto.

Industry/Entity Type

Fast-food

Colors

Designer to choose colors to be used in the design.

Requirements
Must have
• Bold, eye-catching fonts for the deals without losing readability. The customers should clearly see what items come with each deal. The background and menu should be kept clean with pops of colour from images around the menu.

```html
<!DOCTYPE html>
<html lang="en">
<head>
<meta charset="utf-8">
<title>Chili Crust Pizza – Menu</title>
<link href="https://fonts.googleapis.com/css2?family=Oswald:wght@400;500;600;700&family=Roboto+Condensed:wght@400;700&family=Playfair+Display:wght@500;700&display=swap" rel="stylesheet">
<style>
:root{
  --red:#d63a40;
  --gold:#f1c862;
  --gold-text:#d6ab55;
  --dark:#333538;
  --ink:#222226;
  --muted:#55565a;
  --paper:#f7f7f7;
  --paper-grey:#eeeeef;
  --stage:#e6e6e6;
}
*{box-sizing:border-box;margin:0;padding:0}
html,body{width:872px;height:1200px;overflow:hidden}
body{background:var(--stage);font-family:"Roboto Condensed",Arial,sans-serif;color:var(--ink);position:relative}
.sheet{position:absolute;left:10px;width:852px;height:574px;display:flex;box-shadow:0 6px 18px rgba(0,0,0,.18)}
.sheet--outside{top:14px}
.sheet--inside{top:612px}
.panel{width:284px;height:100%;position:relative;padding:16px 18px;overflow:hidden;
  background:linear-gradient(135deg,#fff 0%,var(--paper) 40%,#fbfbfb 60%,var(--paper-grey) 100%)}
.panel + .panel{border-left:1px solid #e2e2e2}
.panel--grey{background:linear-gradient(135deg,#ededee,#e4e4e6 60%,#ececed)}
.panel--dark{background:var(--dark);padding:0}

/* photo placeholders */
.photo{display:block}
.photo--pizza{border-radius:50%;background:radial-gradient(circle at 45% 40%,#e9a658,#c9662f 60%,#9b4a22)}

/* featured deals */
.feature{text-align:center;font-family:"Oswald",sans-serif}
.feature__pizza{width:92px;height:92px;margin:0 auto 8px}
.feature__title{color:var(--red);font-weight:700;font-size:19px;line-height:1.05}
.feature__items{font-weight:600;font-size:13px;line-height:1.2;text-transform:uppercase;color:var(--ink)}
.feature__price{color:var(--red);font-weight:700;font-size:34px;line-height:1.05}
.feature__price small{font-size:20px;margin-right:4px}

/* deals list */
.section-title{font-family:"Playfair Display",serif;font-weight:500;letter-spacing:1.5px;text-transform:uppercase;color:var(--ink);text-align:center}
.deals__heading{font-size:18px;margin:32px 0 14px}
.deal{margin-bottom:9px}
.deal__name{font-family:"Oswald",sans-serif;font-weight:600;font-size:7.8px;text-transform:uppercase;letter-spacing:.2px}
.deal__row{display:flex;justify-content:space-between;align-items:flex-end;gap:6px;font-size:5.8px;color:var(--muted)}
.price{font-family:"Oswald",sans-serif;font-weight:600;color:var(--red);font-size:7.5px;white-space:nowrap}
.collection{background:var(--gold);border-radius:0 14px 0 14px;padding:8px 12px 10px;margin-top:10px;font-family:"Oswald",sans-serif}
.collection__title{text-align:center;font-weight:700;font-size:14px;margin-bottom:4px}
.collection__cols{display:flex;gap:14px;font-size:7px;font-weight:600;text-transform:uppercase}
.collection__cols .price{font-size:7px}
.collection__line{display:flex;gap:8px;line-height:1.45}
.collection__kids{font-family:"Roboto Condensed",sans-serif;text-transform:none;font-weight:400;font-size:6.6px;line-height:1.5}

/* cover */
.cover__badge{position:absolute;left:58px;top:4px;width:112px;height:114px;background:var(--gold);
  clip-path:polygon(0 0,100% 0,100% 80%,50% 100%,0 80%);display:flex;align-items:center;justify-content:center;text-align:center}
.cover__name{font-family:"Oswald",sans-serif;font-weight:700;font-size:16px;line-height:1.05;color:var(--red);text-transform:uppercase;margin-top:-10px}
.cover__details{position:absolute;top:152px;left:0;width:100%;text-align:center;color:var(--gold-text);font-family:"Playfair Display",serif;text-transform:uppercase}
.cover__site{font-size:9.5px;letter-spacing:2px}
.cover__phone{font-size:23px;border-top:1px solid var(--gold-text);border-bottom:1px solid var(--gold-text);margin:4px 20px 6px;padding:2px 0;letter-spacing:.5px}
.cover__address{font-size:9.5px;letter-spacing:1.6px;line-height:1.35}
.cover__pizza{position:absolute;left:0;bottom:0;width:100%;height:236px;background:radial-gradient(ellipse at 60% 55%,#e7a95b,#c0542b 55%,#6b4a33 85%,var(--dark) 100%)}

/* inside */
.menu-title{font-size:14px;margin:2px 0 9px;white-space:nowrap}
.bases{display:flex;justify-content:space-between;text-align:center;font-family:"Oswald",sans-serif;font-size:5.5px;font-weight:500;text-transform:uppercase}
.base__photo{width:28px;height:24px;margin:0 auto 3px;background:linear-gradient(135deg,#e1a863,#b7552e)}
.sizes{display:flex;justify-content:space-between;font-family:"Oswald",sans-serif;font-size:6px;font-weight:600;text-align:center}
.sizes span small{display:block;color:var(--red);font-size:5px}
.sizes--bases{margin:5px 0 10px 100px}
.toppings{display:flex;gap:8px;align-items:center;margin-bottom:6px}
.toppings__photo{width:92px;height:68px;background:radial-gradient(circle at 50% 50%,#e8ad62,#c4592c 60%,transparent 72%)}
.toppings__margherita{font-family:"Oswald",sans-serif;font-weight:600;font-size:8px}
.pizza-list{margin-top:12px;font-size:6.2px;line-height:1.42;color:var(--muted)}
.pizza-list b{color:var(--ink);font-family:"Oswald",sans-serif;font-weight:600;text-transform:uppercase}
.extras{border:1px solid #bdbdc0;border-radius:4px;padding:5px 6px;margin-top:9px;font-size:5.4px;line-height:1.35;color:var(--muted)}
.extras b{color:var(--ink);font-family:"Oswald",sans-serif;font-weight:600}
.extras .sizes{margin-top:5px}

.item{display:flex;justify-content:space-between;align-items:flex-start;gap:6px;margin-bottom:7px}
.item__name{font-family:"Oswald",sans-serif;font-weight:600;font-size:7.4px;text-transform:uppercase}
.item__name small{font-family:"Roboto Condensed",sans-serif;text-transform:none;font-weight:400;font-size:5.7px;color:var(--muted)}
.item__note{display:block;font-family:"Roboto Condensed",sans-serif;text-transform:none;font-weight:400;font-size:5.4px;color:var(--muted);line-height:1.35}
.item .price{font-size:7.4px}
.size-head{text-align:right;font-size:5px;color:var(--muted);text-transform:uppercase;margin-bottom:1px}
.banner{background:var(--red);color:#fff;border-radius:0 8px 0 8px;padding:4px 10px;margin:8px 0 12px;font-size:5.6px}
.banner b{font-family:"Oswald",sans-serif;font-size:7px;text-transform:uppercase}
.menu-title--spaced{margin-top:16px}
.showcase{position:absolute;left:18px;right:14px;bottom:12px;height:110px;background:linear-gradient(90deg,rgba(247,247,247,0) 0%,#e3a552 25%,#c4772e 55%,#4a1d14 80%,rgba(247,247,247,0) 100%);border-radius:8px}
</style>
</head>
<body>

<!-- OUTSIDE -->
<section class="sheet sheet--outside">
  <div class="panel">
    <div class="feature">
      <div class="feature__pizza photo photo--pizza" role="img" aria-label="Photo of a topped pizza"></div>
      <div class="feature__title">PERSONAL MEAL</div>
      <div class="feature__items">Any 10″ Pizza<br>+ 8pcs Chicken<br>+ 1 Can</div>
      <div class="feature__price"><small>£</small>14.99</div>
    </div>
    <div class="feature" style="margin-top:8px">
      <div class="feature__pizza photo photo--pizza" role="img" aria-label="Photo of a topped pizza"></div>
      <div class="feature__title">BARGAIN MEAL</div>
      <div class="feature__items">Any 18″ Pizza<br>+ Side Order<br>+ 1 Large Bottle</div>
      <div class="feature__price"><small>£</small>21.99</div>
    </div>
    <div class="feature" style="margin-top:8px">
      <div class="feature__title">MADNESS DEAL</div>
      <div class="feature__items">2 x 18″ Pizza<br>+2 Side Orders<br>+ 1 Large Bottle</div>
      <div class="feature__price"><small>£</small>38.99</div>
    </div>
  </div>

  <div class="panel">
    <h2 class="section-title deals__heading">Deals Deals Deals</h2>
    <div class="deal"><div class="deal__name">Lunch Time Deal (until 4pm)</div><div class="deal__row"><span>10″ Pizza + Fries + 1 Can</span><span class="price">£9.99</span></div></div>
    <div class="deal"><div class="deal__name">All for 2</div><div class="deal__row"><span>2x 7″ Pizzas + 4pcs Garlic Bread with Cheese + 8pcs BBQ Wings + 2 Cans</span><span class="price">£19.99</span></div></div>
    <div class="deal"><div class="deal__name">Big Saver Deal</div><div class="deal__row"><span>Any Pizza (10″ / 13″ / 15″)<br>+ 1 Side + 1 Large Bottle + 2 dips</span><span class="price">£16.99 / £18.99 / £20.99</span></div></div>
    <div class="deal"><div class="deal__name">Family Meal</div><div class="deal__row"><span>15″ Pizza + 8pcs Chicken + Potato Wedges + Coleslaw + Large Bottle</span><span class="price">£23.99</span></div></div>
    <div class="deal"><div class="deal__name">Square Deal</div><div class="deal__row"><span>2x 13″ Pizzas + Fries + Large Bottle</span><span class="price">£27.99</span></div></div>
    <div class="deal"><div class="deal__name">2's Special</div><div class="deal__row"><span>Any 2x Pizzas (10″ / 13″ / 15″ / 18″)</span><span class="price">£18.99 / £22.99 / £25.99 / £30.99</span></div></div>
    <div class="deal"><div class="deal__name">Triple Deal</div><div class="deal__row"><span>Any 3x Pizzas (10″/13″/15″/18″)</span><span class="price">£24.99 / £28.99 / £33.99 / £42.99</span></div></div>
    <div class="deal"><div class="deal__name">Chili Crust Deal</div><div class="deal__row"><span>3x 10″ Pizzas + 2x Garlic Bread + 12pcs Chicken + Large Bottle</span><span class="price">£32.99</span></div></div>
    <div class="deal"><div class="deal__name">Red Party Deal</div><div class="deal__row"><span>2x 15″ Pizzas + 2 Sides + 1 Large Bottle</span><span class="price">£34.99</span></div></div>
    <div class="deal"><div class="deal__name">Big Family Deal</div><div class="deal__row"><span>2x 18″ Pizzas, 13″ Garlic Pizza Bread with Cheese + 2 Fries + Large Bottle</span><span class="price">£39.99</span></div></div>
    <div class="collection">
      <div class="collection__title">COLLECTION DEALS</div>
      <div class="collection__cols">
        <div>
          <div class="collection__line"><span>Any 7″ Pizza</span><span class="price">£5.50</span></div>
          <div class="collection__line"><span>Any 10″ Pizza</span><span class="price">£6.99</span></div>
          <div class="collection__line"><span>Any 13″ Pizza</span><span class="price">£8.99</span></div>
          <div class="collection__line"><span>Any 15″ Pizza</span><span class="price">£10.99</span></div>
          <div class="collection__line"><span>Any 18″ Pizza</span><span class="price">£13.99</span></div>
        </div>
        <div style="padding-top:10px">
          <div class="collection__line"><span>Kids Meals</span><span class="price">£5.90</span></div>
          <div class="collection__kids">• 7″ Margherita + 1 Can<br>• 4pcs Chicken + Fries + 1 Can</div>
        </div>
      </div>
    </div>
  </div>

  <div class="panel panel--dark">
    <div class="cover__badge"><div class="cover__name">Chili Crust<br>Pizza</div></div>
    <div class="cover__details">
      <div class="cover__site">chilicrustpizza.co.uk</div>
      <div class="cover__phone">0208 555 0142</div>
      <div class="cover__address">24 Marlow Lane,<br>Elmstead EL4 2QP</div>
    </div>
    <div class="cover__pizza photo" role="img" aria-label="Large photo of a pepperoni pizza on a wooden board"></div>
  </div>
</section>

<!-- INSIDE -->
<section class="sheet sheet--inside">
  <div class="panel panel--grey">
    <h2 class="section-title menu-title">1. Pick Your Base</h2>
    <div class="bases">
      <div><div class="base__photo photo" role="img" aria-label="Deep pan base"></div>Deep Pan</div>
      <div><div class="base__photo photo" role="img" aria-label="Thin crust base"></div>Thin Crust</div>
      <div><div class="base__photo photo" role="img" aria-label="Cheese crust base"></div>Cheese<br>Crust</div>
      <div><div class="base__photo photo" role="img" aria-label="Pepperoni crust base"></div>Pepperoni<br>Crust</div>
      <div><div class="base__photo photo" role="img" aria-label="Hotdog crust base"></div>Hotdog<br>Crust</div>
    </div>
    <div class="sizes sizes--bases"><span>7″<small>+£0.99</small></span><span>10″<small>+£1.99</small></span><span>13″<small>+£2.49</small></span><span>15″<small>+£2.99</small></span><span>18″<small>+£3.99</small></span></div>

    <h2 class="section-title menu-title">2. Pick Your Toppings</h2>
    <div class="toppings">
      <div class="toppings__photo photo" role="img" aria-label="Photo of pizza slices"></div>
      <div style="flex:1">
        <div class="toppings__margherita">Margherita – Cheese &amp; Tomato</div>
        <div class="sizes" style="margin-top:3px"><span>7″<small>+£5.99</small></span><span>10″<small>+£7.99</small></span><span>13″<small>+£9.49</small></span><span>15″<small>+£11.99</small></span><span>18″<small>+£15.99</small></span></div>
      </div>
    </div>
    <div class="sizes"><span>7″<small>+£5.99</small></span><span>10″<small>+£7.99</small></span><span>13″<small>+£9.99</small></span><span>15″<small>+£11.99</small></span><span>18″<small>+£15.99</small></span></div>

    <div class="pizza-list">
      <b>Make Your Own</b> – Any 4 toppings of your choice<br>
      <b>Pepperoni Passion</b> – Double Pepperoni, Double Cheese<br>
      <b>Hawaiian</b> – Ham, Mushrooms, Pineapple<br>
      <b>House Special</b> – ?<br>
      <b>Coriander Chilli Chicken</b> – Garlic Butter, Chicken Tikka, Red Onions, Chillies, Fresh Coriander<br>
      <b>Vegetarian</b> – Red Onions, Mushrooms, Mixed Peppers, Sweetcorn, Fresh Tomatoes<br>
      <b>Veggie Volcano</b> – Garlic Butter Base, Red Onions, Mixed Peppers, Black Olives, Fresh Tomatoes, Chillies<br>
      <b>Mexican Spice</b> – Spicy Beef, Mexican Chicken, Red Onions, Mixed Peppers, Jalapeños, Fresh Tomatoes<br>
      <b>Meat Feast</b> – Pepperoni, Ham, Spicy Pork, Spicy Beef<br>
      <b>Alligator</b> – Salami, Pepperoni, Ham, Smoky Sausage, Bacon<br>
      <b>Greek Style</b> – Pepperoni, Red Onions, Black Olives, Fresh Tomatoes, Feta Cheese, Mixed Herbs<br>
      <b>Oriental Express</b> – Chinese Chicken, Mushrooms, Mixed Peppers, Sweetcorn, Pineapple<br>
      <b>BBQ Feast</b> – BBQ Sauce, Pepperoni, Meatballs, Red Onions<br>
      <b>BBQ Chicken Sizzler</b> – BBQ Sauce, Bacon, Chicken, Red Onions<br>
      <b>Caribbean Tuna</b> – Red Onions, Mixed Peppers, Jalapeños, Fresh Tomatoes, Tuna<br>
      <b>Space for another pizza</b> – lorem ipsum<br>
      <b>Space for another pizza</b> – lorem ipsum
    </div>
    <div class="extras">
      <b>EXTRA TOPPINGS</b> – Garlic Butter, Pizza Sauce, BBQ Sauce, Cheese, Salami, Pepperoni, Ham, Kebab, Smoky Sausage, Meatballs, Bacon, Spicy Pork, Chicken, Spicy Beef, Chinese Chicken, Chicken Tikka, Tandoori Chicken, Red Onions, Mushrooms, Mixed Peppers, Pineapple, Sweetcorn, Jalapeños, Black Olives, Feta, Tuna, Cheese, Chillies, Fresh Garlic, Mixed Herbs, Fresh Coriander, Prawns, Anchovies, Fresh Tomatoes
      <div class="sizes"><span>7″<small>+£0.79</small></span><span>10″<small>+£0.99</small></span><span>13″<small>+£1.29</small></span><span>15″<small>+£1.49</small></span><span>18″<small>+£1.79</small></span></div>
    </div>
  </div>

  <div class="panel">
    <h2 class="section-title menu-title">3. Side Orders</h2>
    <div class="size-head">Single / Double up</div>
    <div class="item"><div class="item__name">Garlic Bread <small>– 4 slices + Add cheese for 50p</small></div><span class="price">£2.94 / £4.49</span></div>
    <div class="item"><div class="item__name">Garlic Pizza Bread <small>– freshly baked 10″ pizza</small><span class="item__note">+ Add cheese for 50p<br>+ Upgrade to a 13″ for £2 extra</span></div><span class="price">£7.99</span></div>
    <div class="item"><div class="item__name">Fries</div><span class="price">£2.99 / £4.99</span></div>
    <div class="item"><div class="item__name">Curly Fries<span class="item__note">+ Add cheese for 50p Wedges – comes with 2 dips Potato Skins with Cheese<br>+ Add a topping for 50p</span></div><span class="price">£4.99 / £8.99</span></div>
    <div class="item"><div class="item__name">Mixed Salad<span class="item__note">+ Add chicken for 99p</span></div><span class="price">£3.99</span></div>
    <div class="item"><div class="item__name">Greek Salad</div><span class="price">£4.99</span></div>
    <div class="item"><div class="item__name">Coleslaw</div><span class="price">£1.99</span></div>
    <div class="item"><div class="item__name">Mozzarella Sticks <small>– 8 pieces</small></div><span class="price">£4.99 / £8.99</span></div>
    <div class="item"><div class="item__name">Onion Rings <small>– 8 pieces</small></div><span class="price">£3.49 / £5.99</span></div>
    <div class="item"><div class="item__name">Cream Cheese Jalapeños <small>– 8 piece</small></div><span class="price">£4.99 / £8.99</span></div>
    <div class="item"><div class="item__name">BBQ Ribs</div><span class="price">£5.99 / £9.99</span></div>
    <div class="banner"><b>Mixed Platter</b> – 3 chicken strips, 3 mozzarella sticks, <b>£10,99</b><br>3 jalapeño cream cheese bites, 6 onion rings, wedges and choice of 2 dips</div>

    <h2 class="section-title menu-title">4. Chicken Sides</h2>
    <div class="item"><div class="item__name">Chicken Strips <small>– 8 pieces</small><span class="item__note">+ Double up for £4.00 extra</span></div><span class="price">£4.99 / £8.99</span></div>
    <div class="item"><div class="item__name">BBQ Wings <small>– 8 pieces</small><span class="item__note">+ Double up for £4.00 extra</span></div><span class="price">£4.99 / £8.99</span></div>
    <div class="item"><div class="item__name">Spicy Chicken Dippers <small>– 8 pieces</small><span class="item__note">+ Double up for £4.00 extra</span></div><span class="price">£4.99 / £8.99</span></div>
    <div class="item"><div class="item__name">Hot Wings <small>– 8 pieces</small><span class="item__note">+ Double up for £4.00 extra</span></div><span class="price">£4.99 / £8.99</span></div>
    <div class="item"><div class="item__name">Chicken Nuggets <small>– 8 pieces</small></div><span class="price">£4.99 / £8.99</span></div>
    <div class="banner"><b>Chicken Combo</b> – Any 6 pieces of chicken and potato wedges &nbsp; <b>£6,99</b></div>
  </div>

  <div class="panel">
    <h2 class="section-title menu-title">5. Pastas</h2>
    <div class="item"><div class="item__name">Meat Lasagne</div><span class="price">£6.99</span></div>
    <div class="item"><div class="item__name">Vegetable Lasagne</div><span class="price">£6.99</span></div>
    <div class="item"><div class="item__name">Spaghetti Bolognese</div><span class="price">£6.99</span></div>
    <div class="item"><div class="item__name">Chicken &amp; Mushroom Pasta</div><span class="price">£6.99</span></div>

    <h2 class="section-title menu-title menu-title--spaced">6. Desserts</h2>
    <div class="item"><div class="item__name">Bramble &amp; Barrow <small>465ml Cookie Dough, Fudge Brownie, Salted Caramel, Choc Chip</small></div><span class="price">£5.99</span></div>
    <div class="item"><div class="item__name">Nordhavn <small>460ml Vanilla, Pralines &amp; Cream, Strawberry Cheesecake, Cookies &amp; Cream</small></div><span class="price">£5.99</span></div>
    <div class="item"><div class="item__name">Strawberry Cheesecake Slice</div><span class="price">£2.99</span></div>
    <div class="item"><div class="item__name">Tennessee Toffee Cake Slice</div><span class="price">£2.99</span></div>
    <div class="item"><div class="item__name">Chocolate Fudge Cake Slice</div><span class="price">£2.99</span></div>
    <div class="item"><div class="item__name">Banoffee Pie Slice</div><span class="price">£2.99</span></div>

    <h2 class="section-title menu-title menu-title--spaced">7. Drinks &amp; Extras</h2>
    <div class="item"><div class="item__name">Cans <small>330ml</small><span class="item__note">Regular Fizzco Cola, Diet Fizzco, Fizzco Zero, Orangeo, Zestlime, Clearup, Bluecap, Doc Spice</span></div><span class="price">£1.25</span></div>
    <div class="item"><div class="item__name">Water <small>500ml</small></div><span class="price">£1.00</span></div>
    <div class="item"><div class="item__name">Bottles <small>1.5 litre Regular Fizzco Cola, Diet Fizzco, Zingo Orange, Clearup, Bluecap</small></div><span class="price">£2.99</span></div>
    <div class="item"><div class="item__name">Dips <small>25g Garlic &amp; Herb, Sour Cream &amp; Chives, BBQ Sauce, Sweet Chilli, Sweet &amp; Sour, Tomato Ketchup, Chilli Sauce</small></div><span class="price">£0.50</span></div>
    <div class="item"><div class="item__name">3 Dips for <span style="color:var(--red)">£1</span></div></div>
    <div class="showcase photo" role="img" aria-label="Photo of fried chicken pieces, a dip and a glass of cola"></div>
  </div>
</section>

</body>
</html>
```